Meadowlyn Acres Website Design

We have been redeveloping our website already and are quite happy with the content, but the design needs to be better:
https://harvo-link.example-host.com/

Pages, content, concept etc. Can all be taken from the redeveloped website.
The farmer can register and edit/view their profile, subscribe and these pages need to be designed better as well as contact, about, pricing, tos, privacy and a page with example portlets.

We need a website to appeal to farmers, investors and retiring farmers.

The design should be clean and a little country.

We don't want any repeat designs that some may submit to every project and has no respect for the project brief, so please don't submit them.

Target Market(s)

farmers, investors, retirees

Industry/Entity Type

Farming

Number of Pages Required

5+ page

Colors

Designer to choose colors to be used in the design.

Requirements
Must have
• Nice, clean modern design that is appealing
• Profile page laid out nicely

```html
<!DOCTYPE html>
<html lang="en">
<head>
<meta charset="utf-8">
<title>Meadowlyn Acres</title>
<link href="https://fonts.googleapis.com/css2?family=Lato:wght@400;700;900&family=Open+Sans:wght@400;600;700&family=Roboto+Condensed:wght@700&display=swap" rel="stylesheet">
<style>
:root{
  --green:#3aa346;
  --green-dark:#1f6a2e;
  --green-deep:#17621f;
  --green-band:#4ea656;
  --mint:#eefbec;
  --ink:#333;
  --muted:#666;
  --white:#fff;
  --footer-bg:#f3f6f3;
  --bar:#e6e6e6;
}
*{box-sizing:border-box;margin:0;padding:0}
html,body{width:1200px;height:3622px;overflow:hidden}
body{font-family:"Open Sans",Arial,sans-serif;color:var(--ink);background:var(--white);position:relative}
section,header,footer{position:relative;width:1200px;overflow:hidden}
.abs{position:absolute}
.btn{position:absolute;display:flex;align-items:center;justify-content:center;font:700 16px "Open Sans",sans-serif;color:var(--white);background:var(--green);border-radius:3px;white-space:nowrap}
.btn.dark{background:var(--green-dark)}
.btn.outline{background:transparent;border:2px solid var(--white)}

/* header */
.site-header{height:133px;border-top:5px solid var(--green)}
.brand{position:absolute;left:99px;top:38px;display:flex;align-items:center;gap:16px}
.brand-dot{width:56px;height:56px;border-radius:50%;background:var(--green)}
.brand-name{font:700 34px "Roboto Condensed",sans-serif;color:var(--green)}
.contact-pill{position:absolute;top:25px;display:flex;align-items:center;gap:9px;font:600 15px "Open Sans",sans-serif;white-space:nowrap}
.contact-pill .ico{width:34px;height:34px;border-radius:50%;background:var(--green);display:flex;align-items:center;justify-content:center;flex:none}
.contact-pill.phone .ico{background:var(--green-dark)}
.main-nav{position:absolute;right:100px;top:94px;display:flex;gap:38px;font:600 15px "Open Sans",sans-serif;color:#222;white-space:nowrap}
.main-nav .active{color:var(--green)}

/* hero */
.hero{height:514px}
.hero-photo{position:absolute;inset:0;background:linear-gradient(180deg,#8ea7a8 0%,#6f8464 38%,#4d6b33 62%,#6d7f3c 100%)}
.hero-title{position:absolute;right:100px;top:108px;font:900 44px "Lato",sans-serif;color:var(--white);text-align:right;white-space:nowrap}
.hero-text{position:absolute;right:100px;top:178px;width:480px;text-align:right;font:600 14px/31px "Open Sans",sans-serif;color:var(--white)}
.hero-dots{position:absolute;left:1010px;top:372px;display:flex;gap:6px}
.hero-dots span{width:16px;height:16px;border-radius:50%;border:2px solid var(--white)}
.hero-dots span.on{background:var(--white)}

/* aspiring */
.aspiring{height:572px;text-align:center}
.kicker{font:600 17px "Open Sans",sans-serif;color:#222;padding-top:63px}
.section-title{font:900 28px "Lato",sans-serif;color:var(--green)}
.title-rule{width:80px;height:3px;background:var(--green);margin:12px auto 0}
.journey{position:absolute;top:215px;left:0;width:1200px}
.journey-item{position:absolute;width:240px;text-align:center}
.journey-photo{width:140px;height:140px;border-radius:50%;margin:0 auto;border:4px solid var(--green)}
.journey-label{margin-top:36px;font:600 20px/1.5 "Open Sans",sans-serif;color:#222}
.journey-label.green{color:var(--green)}

/* subscribe */
.subscribe{height:543px;background:linear-gradient(180deg,#55ad5c,#3f9a48)}
.subscribe-photo{position:absolute;left:99px;top:68px;width:393px;height:403px;border:4px solid #e8f4e8;background:linear-gradient(160deg,#b49b84,#7a5d4a 55%,#c9c0b5)}
.subscribe-copy{position:absolute;left:541px;top:65px;width:560px;color:var(--white)}
.subscribe-copy h2{font:700 26px/1.4 "Lato",sans-serif}
.subscribe-copy .rule{width:120px;height:2px;background:var(--white);margin:18px 0 14px}
.perks{list-style:none;font:14.5px/2.4 "Open Sans",sans-serif}
.perks li{display:flex;align-items:center;gap:14px}
.perks li::before{content:"";width:12px;height:12px;border-radius:50%;border:2px solid var(--white);flex:none}

/* how it works */
.how{height:616px;text-align:center}
.how .section-title{padding-top:72px}
.step-circle{position:absolute;border-radius:50%;display:flex;align-items:center;justify-content:center}
.step-circle.light{width:156px;height:156px;background:var(--green);box-shadow:0 0 0 5px var(--white),0 0 0 8px var(--green)}
.step-circle.dark{width:160px;height:160px;background:var(--green-dark);box-shadow:0 0 0 5px var(--white),0 0 0 8px var(--green-dark)}
.step-name{position:absolute;font:700 20px "Lato",sans-serif;color:var(--green);width:300px;text-align:center}
.step-name.dark{color:#222}
.step-text{position:absolute;width:320px;text-align:center;font:13px/1.6 "Open Sans",sans-serif;color:#444}
.tag{position:absolute;display:flex;align-items:center;justify-content:center;font:700 14px "Open Sans",sans-serif;color:var(--white);border-radius:2px}

/* investors */
.investors{height:483px;background:var(--mint)}
.video{position:absolute;left:99px;top:84px;width:541px;height:307px;background:linear-gradient(135deg,#8a6a4e,#4b3526 60%,#2c2018)}
.video-bar{position:absolute;left:0;bottom:0;width:100%;height:24px;background:rgba(0,0,0,.75)}
.video-bar .prog{position:absolute;left:0;top:0;width:34%;height:3px;background:#d22}
.investors-copy{position:absolute;left:676px;top:82px;width:440px}
.investors-copy h2{font:900 28px "Lato",sans-serif;color:var(--green)}
.investors-copy .rule{width:60px;height:3px;background:var(--green);margin:10px 0 22px}
.investors-copy p{font:14.5px/1.75 "Open Sans",sans-serif;color:#333}
.investors-copy p.lead{color:var(--green);margin-top:14px}

/* retiring */
.retiring{height:362px;background:linear-gradient(180deg,#1e7a2a,#17661f);text-align:center;color:var(--white)}
.retiring h2{font:900 28px "Lato",sans-serif;padding-top:72px}
.retiring .rule{width:60px;height:3px;background:var(--white);margin:12px auto 22px}
.retiring p{font:600 15.5px/1.9 "Open Sans",sans-serif;width:1000px;margin:0 auto}

/* footer */
.site-footer{height:338px;background:var(--footer-bg)}
.footer-map{position:absolute;left:0;top:0;width:560px;height:338px;background:radial-gradient(ellipse at 40% 40%,#e7ece7,#f3f6f3 70%)}
.footer-brand{position:absolute;left:99px;top:150px;display:flex;align-items:center;gap:14px}
.footer-brand .brand-dot{width:46px;height:46px}
.footer-brand .brand-name{font-size:30px}
.footer-col{position:absolute;top:53px}
.footer-col h3{font:700 16px "Lato",sans-serif;color:var(--green);letter-spacing:.5px}
.footer-col .rule{width:40px;height:2px;background:var(--green);margin:8px 0 12px}
.footer-col ul{list-style:none;font:14px/2.2 "Open Sans",sans-serif;color:#333}
.footer-col li::before{content:"› ";}
.field{position:absolute;background:var(--white);border:1px solid #bbb;font:13px "Open Sans",sans-serif;color:#444;padding:8px 10px}
.bottom-bar{position:absolute;left:0;top:3561px;width:1200px;height:61px;background:var(--bar)}
.bottom-bar .copy{position:absolute;left:99px;top:21px;font:13px "Open Sans",sans-serif;color:#333}
.socials{position:absolute;right:100px;top:14px;display:flex;gap:8px}
.socials span{width:32px;height:32px;border-radius:50%;border:2px solid #444}
.edge{position:absolute;left:0;width:1200px;height:16px}
</style>
</head>
<body>

<header class="site-header">
  <div class="brand"><span class="brand-dot"></span><span class="brand-name">Meadowlyn Acres</span></div>
  <div class="contact-pill" style="left:690px">
    <span class="ico"><svg width="18" height="14" viewBox="0 0 18 14"><rect x="1" y="1" width="16" height="12" rx="1" fill="none" stroke="#fff" stroke-width="2"/><path d="M1 2l8 6 8-6" fill="none" stroke="#fff" stroke-width="2"/></svg></span>
    <span>info@meadowlynacres.com</span>
  </div>
  <div class="contact-pill phone" style="left:960px">
    <span class="ico"><svg width="16" height="16" viewBox="0 0 24 24"><path d="M6.6 10.8a15 15 0 006.6 6.6l2.2-2.2c.3-.3.7-.4 1-.2 1.1.4 2.3.6 3.6.6.6 0 1 .4 1 1V20c0 .6-.4 1-1 1A17 17 0 013 4c0-.6.4-1 1-1h3.5c.6 0 1 .4 1 1 0 1.3.2 2.5.6 3.6.1.3 0 .7-.2 1z" fill="#fff"/></svg></span>
    <span>1800 555 0142</span>
  </div>
  <nav class="main-nav">
    <span class="active">Home</span><span>Aspiring Farmers</span><span>Investors</span><span>Retiring Farmer</span><span>Blogs</span><span>Pricing</span>
  </nav>
</header>

<section class="hero">
  <div class="hero-photo" role="img" aria-label="Photo of a farming family with a horse and cattle on a green pasture"></div>
  <h1 class="hero-title">MEADOWLYN ACRES</h1>
  <p class="hero-text">We know how hard it is for a young family to find the capital<br>required to own and operate their own farm</p>
  <div class="btn" style="left:958px;top:280px;width:142px;height:48px;border:2px solid #fff">Read More</div>
  <div class="hero-dots"><span class="on"></span><span></span><span></span><span></span><span></span></div>
</section>

<section class="aspiring">
  <p class="kicker">Aspiring Farmers</p>
  <h2 class="section-title">YOU CAN OWN A FARM</h2>
  <div class="title-rule"></div>
  <div class="journey">
    <div class="journey-item" style="left:72px">
      <div class="journey-photo" role="img" aria-label="Photo of a young farming family" style="background:linear-gradient(135deg,#c8554a,#7b4b3a)"></div>
      <p class="journey-label">We connect a young<br>farming family</p>
    </div>
    <div class="journey-item" style="left:343px">
      <div class="journey-photo" role="img" aria-label="Photo of a retiring farming family" style="background:linear-gradient(135deg,#6b8a55,#384a32)"></div>
      <p class="journey-label green">with a retiring<br>farming family</p>
    </div>
    <div class="journey-item" style="left:614px">
      <div class="journey-photo" role="img" aria-label="Photo of a farm shed interior" style="background:linear-gradient(135deg,#8c6a4a,#4a3a2c)"></div>
      <p class="journey-label">and investors</p>
    </div>
    <div class="journey-item" style="left:885px">
      <div class="journey-photo" role="img" aria-label="Photo of open farmland under blue sky" style="background:linear-gradient(180deg,#5d8fd6,#9cc1e8 45%,#5c7f3a 60%)"></div>
      <p class="journey-label green">to own and operate<br>a farm together</p>
    </div>
  </div>
</section>

<section class="subscribe">
  <svg class="edge" style="top:0" viewBox="0 0 1200 16" preserveAspectRatio="none" aria-hidden="true"><defs><pattern id="zz1" width="20" height="16" patternUnits="userSpaceOnUse"><path d="M0 0h20v6l-10 8-10-8z" fill="#fff"/></pattern></defs><rect width="1200" height="16" fill="url(#zz1)"/></svg>
  <div class="subscribe-photo" role="img" aria-label="Photo of two young farmers baking in a kitchen"></div>
  <div class="subscribe-copy">
    <h2>Subscribe to be Either an Aspiring or Premium<br>Farmer to Receive:</h2>
    <div class="rule"></div>
    <ul class="perks">
      <li>Free Agrilens market analysis membership (valued at $300 pa)</li>
      <li>Farm business webinars (valued at $200)</li>
      <li>Corporate Partner Opportunities</li>
      <li>Public or Private profile (as required)</li>
      <li>Eligible to enter competitions and win prizes</li>
      <li>...and more. Visit our pricing page to find out more</li>
    </ul>
    <div class="btn" style="position:relative;margin-top:18px;width:134px;height:48px;background:var(--green-dark);border:2px solid #fff">JOIN NOW</div>
  </div>
  <svg class="edge" style="bottom:0" viewBox="0 0 1200 16" preserveAspectRatio="none" aria-hidden="true"><defs><pattern id="zz2" width="20" height="16" patternUnits="userSpaceOnUse"><path d="M0 16h20v-6l-10-8-10 8z" fill="#fff"/></pattern></defs><rect width="1200" height="16" fill="url(#zz2)"/></svg>
</section>

<section class="how">
  <h2 class="section-title">HOW IT WORKS</h2>
  <div class="title-rule"></div>

  <div class="step-circle light" style="left:188px;top:200px">
    <svg width="80" height="60" viewBox="0 0 80 60"><path d="M6 30L30 10l24 20" fill="none" stroke="#fff" stroke-width="4"/><rect x="14" y="28" width="32" height="24" fill="none" stroke="#fff" stroke-width="4"/><rect x="25" y="38" width="10" height="14" fill="#fff"/><circle cx="64" cy="18" r="8" fill="none" stroke="#fff" stroke-width="3"/><path d="M64 26v26" stroke="#fff" stroke-width="3"/></svg>
  </div>
  <p class="step-name" style="left:116px;top:398px">Step 1</p>
  <p class="step-text" style="left:106px;top:444px">Register as an Aspiring Farmer</p>
  <div class="btn" style="left:208px;top:487px;width:112px;height:42px;font-size:14px">REGISTER</div>

  <div class="tag" style="left:536px;top:184px;width:130px;height:43px;background:var(--green-dark)">FARM-READY</div>
  <p class="step-text" style="left:441px;top:242px">Build your farm skills to get yourself<br>farm-ready.</p>
  <p class="step-name dark" style="left:451px;top:294px">Step 2</p>
  <div class="step-circle dark" style="left:521px;top:350px">
    <svg width="78" height="66" viewBox="0 0 78 66"><path d="M6 22l6-14h46l6 14z" fill="none" stroke="#fff" stroke-width="4"/><rect x="12" y="24" width="46" height="30" fill="none" stroke="#fff" stroke-width="4"/><path d="M20 34h18M20 42h12" stroke="#fff" stroke-width="4"/><path d="M58 36a10 10 0 0120 0c0 8-10 18-10 18s-10-10-10-18z" fill="#fff"/><circle cx="68" cy="36" r="4" fill="var(--green-dark)"/></svg>
  </div>

  <div class="step-circle light" style="left:859px;top:207px">
    <svg width="76" height="60" viewBox="0 0 76 60"><path d="M8 26L38 6l30 20" fill="none" stroke="#fff" stroke-width="4"/><path d="M14 26v28M62 26v28" stroke="#fff" stroke-width="4"/><path d="M20 40l10-8 8 6 8-6 10 8-10 8h-16z" fill="#fff"/></svg>
  </div>
  <p class="step-name" style="left:787px;top:405px">Step 3</p>
  <p class="step-text" style="left:777px;top:451px">Together we find you your dream farm.</p>
  <div class="btn" style="left:863px;top:494px;width:148px;height:42px;font-size:14px">MATCH-MAKING</div>

  <svg class="abs" style="left:372px;top:330px" width="140" height="80" viewBox="0 0 140 80" aria-hidden="true"><path d="M6 10c30 0 70 20 118 56" fill="none" stroke="#bbb" stroke-width="4"/><path d="M108 64l18 4-4-18" fill="none" stroke="#bbb" stroke-width="4"/></svg>
  <svg class="abs" style="left:698px;top:338px" width="140" height="70" viewBox="0 0 140 70" aria-hidden="true"><path d="M6 60c30-40 80-50 118-30" fill="none" stroke="#bbb" stroke-width="4"/><path d="M106 20l20 10-14 14" fill="none" stroke="#bbb" stroke-width="4"/></svg>
</section>

<section class="investors">
  <div class="video" role="img" aria-label="Video still of a young farmer speaking indoors">
    <div class="video-bar"><span class="prog"></span></div>
  </div>
  <div class="investors-copy">
    <h2>INVESTORS</h2>
    <div class="rule"></div>
    <p>We have the best farmers in Australia ready to work with you on your farm. Simply browse the list and decide who you want to work with. No registration required and your information will be kept private</p>
    <p class="lead">Get in touch discuss the best farm succession opportunity for you</p>
  </div>
  <div class="btn" style="left:676px;top:335px;width:124px;height:46px">Signup Now</div>
  <div class="btn dark" style="left:813px;top:335px;width:138px;height:46px">Find Out More</div>
</section>

<section class="retiring">
  <h2>RETIRING FARMERS</h2>
  <div class="rule"></div>
  <p>Are you looking for a positive way to step back from your farm? We can connect you with a passionate aspiring farming family who will love your farm just as much as you do. No registration required and your information will be kept private</p>
  <div class="btn outline" style="left:460px;top:236px;width:126px;height:46px">Enquire Now</div>
  <div class="btn outline" style="left:600px;top:236px;width:140px;height:46px">Find Out More</div>
  <svg class="edge" style="bottom:0" viewBox="0 0 1200 16" preserveAspectRatio="none" aria-hidden="true"><defs><pattern id="zz3" width="20" height="16" patternUnits="userSpaceOnUse"><path d="M0 16h20v-6l-10-8-10 8z" fill="#f3f6f3"/></pattern></defs><rect width="1200" height="16" fill="url(#zz3)"/></svg>
</section>

<footer class="site-footer">
  <div class="footer-map" role="img" aria-label="Faint map of Australia"></div>
  <div class="footer-brand"><span class="brand-dot"></span><span class="brand-name">Meadowlyn Acres</span></div>
  <div class="footer-col" style="left:444px">
    <h3>QUICK LINKS</h3><div class="rule"></div>
    <ul><li>Home</li><li>Farmers</li><li>Investors</li><li>Retiring</li><li>About</li><li>Pricing</li></ul>
  </div>
  <div class="footer-col" style="left:606px">
    <h3>SUPPORT</h3><div class="rule"></div>
    <ul><li>Contact</li><li>Terms of Service</li><li>Privacy</li><li>Newsletter</li></ul>
  </div>
  <div class="footer-col" style="left:813px">
    <h3>CONTACT FORM</h3><div class="rule"></div>
  </div>
  <div class="field" style="left:813px;top:110px;width:138px;height:38px">Name</div>
  <div class="field" style="left:961px;top:110px;width:138px;height:38px">Phone</div>
  <div class="field" style="left:813px;top:158px;width:286px;height:66px">Message</div>
  <div class="btn" style="left:813px;top:238px;width:120px;height:38px;font-size:12px">SEND MESSAGE</div>
</footer>

<div class="bottom-bar">
  <p class="copy">Copyright © 2017 Meadowlyn Acres. All Right Reserved</p>
  <div class="socials"><span></span><span></span><span></span><span></span><span></span></div>
</div>

</body>
</html>
```